Velvet Lantern - listen to podcasts from around the world

http://randompodcasts.com/Velvet Lantern lets you listen to randomly selected podcasts from around the world. You can filter the podcasts by language. The power of randomness allows you to escape filter bubbles and echo chambers and discover issues and perspectives that you never knew existed. The current website offers basic functionality and is only a demo. Don't assume that anything in the current "design" should stay in place. The goal of the design should be to make it as easy as possible to understand what the app offers, to listen to new podcasts, and to skip to the next podcast. The service will be offered both as mobile apps and directly on the website. We expect that most users will be on mobile devices which is why we are focusing on the mobile/web app design.In addition to the current functionality, the app should also offer search (allowing the user to listen to podcasts that match given keywords), allow the user to easily subscribe to the current podcast and show the profile picture of the current podcast.

Target Market(s)

People interested in podcasts, all around the world

Colors

Designer to choose colors to be used in the design.

Requirements
Must have
• The main challenge is how to communicate the concept of the app to the user. Podcasts are randomly selected and the user just skips to the next one when he/she wants to. The ability to filter podcasts by language is important but no other filters are needed. The point is to use the power of random selection to explore new surprising content.
Nice to have
• The app/website is targeting a global audience. The less reliant the design is on written language, the better.

```html
<!DOCTYPE html>
<html lang="en">
<head>
<meta charset="utf-8">
<title>Velvet Lantern – mobile screens</title>
<link href="https://fonts.googleapis.com/css2?family=Fira+Sans+Condensed:wght@400;600;700&family=Fira+Sans:wght@400;600&family=Noto+Serif:wght@400;700&family=PT+Serif:wght@400;700&display=swap" rel="stylesheet">
<style>
:root{
  --stage:#8a8a8a;
  --frame:#ffffff;
  --screen:#f3f3f3;
  --card:#ffffff;
  --ink:#111111;
  --text:#333333;
  --muted:#777777;
  --navy:#0d3a5c;
  --map:#e2e2e2;
  --line:#ececec;
  --danger:#f7d9d9;
  --danger-ink:#e06a6a;
  --flag-blue:#1f3f91;
  --flag-red:#d52b2b;
  --flag-yellow:#f2c200;
  --flag-green:#1e8a3a;
}
*{box-sizing:border-box;margin:0;padding:0}
html,body{width:1200px;height:1198px;overflow:hidden;background:var(--stage)}
body{position:relative;font-family:"Fira Sans",sans-serif;color:var(--text)}
.phone{position:absolute;width:268px;height:566px;background:var(--screen);border:6px solid var(--frame);border-radius:34px;overflow:hidden}
.phone *{position:absolute}
.phone b,.phone span,.phone i{position:static}
.status-time{top:14px;left:24px;font-size:7px;color:#bbb}
.notch{top:-6px;left:58px;width:140px;height:26px;background:var(--frame);border-radius:0 0 16px 16px}
.home-bar{bottom:8px;left:84px;width:88px;height:2px;border-radius:2px;background:#e4e4e4}
.world-map{left:12px;width:240px;height:160px;border-radius:40% 50% 45% 40%;background:radial-gradient(ellipse at 50% 50%,var(--map) 0%,#ececec 55%,var(--screen) 75%)}
.brand-mark{left:113px;width:38px;height:38px;border-radius:50%;background:var(--ink)}
.app-title{left:0;width:256px;text-align:center;font-family:"Fira Sans Condensed",sans-serif;font-weight:700;font-size:12.5px;color:var(--ink)}
.app-tagline{left:0;width:256px;text-align:center;font-family:"Noto Serif",serif;font-size:7.6px;line-height:12px;color:#444}
.divider{left:113px;width:32px;height:1px;background:#333}
.play-btn{left:111px;width:34px;height:34px;border-radius:50%;background:var(--navy)}
.play-btn svg{left:12px;top:10px}
.lang-row{left:27px;width:213px;height:33px;background:var(--card);border-bottom:1px solid var(--line)}
.lang-row .flag{left:10px;top:12px;width:17px;height:10px}
.lang-row .label{left:32px;top:11px;font-family:"Fira Sans Condensed",sans-serif;font-size:7.6px;font-weight:700;color:var(--ink);white-space:nowrap;text-transform:uppercase}
.lang-row .label span{font-weight:400;color:#555}
.lang-row .ctrl{right:10px;top:9px}
.flag-uk{background:linear-gradient(var(--flag-red),var(--flag-red)) center/100% 2px no-repeat,linear-gradient(var(--flag-red),var(--flag-red)) center/2px 100% no-repeat,linear-gradient(#fff,#fff) center/100% 4px no-repeat,linear-gradient(#fff,#fff) center/4px 100% no-repeat,var(--flag-blue)}
.flag-de{background:linear-gradient(#000 33%,var(--flag-red) 33% 66%,var(--flag-yellow) 66%)}
.flag-es{background:linear-gradient(var(--flag-red) 25%,var(--flag-yellow) 25% 75%,var(--flag-red) 75%)}
.flag-fr{background:linear-gradient(90deg,var(--flag-blue) 33%,#fff 33% 66%,var(--flag-red) 66%)}
.flag-pt{background:linear-gradient(90deg,var(--flag-green) 40%,var(--flag-red) 40%)}
.flag-se{background:linear-gradient(var(--flag-yellow),var(--flag-yellow)) center/100% 2px no-repeat,linear-gradient(var(--flag-yellow),var(--flag-yellow)) 6px 0/2px 100% no-repeat,#1d67b1}
.flag-cn{background:var(--flag-red)}
.flag-ru{background:linear-gradient(#fff 33%,var(--flag-blue) 33% 66%,var(--flag-red) 66%)}
.flag-dk{background:linear-gradient(#fff,#fff) center/100% 2px no-repeat,linear-gradient(#fff,#fff) 6px 0/2px 100% no-repeat,var(--flag-red)}
.flag-nl{background:linear-gradient(var(--flag-red) 33%,#fff 33% 66%,var(--flag-blue) 66%)}
.flag-it{background:linear-gradient(90deg,var(--flag-green) 33%,#fff 33% 66%,var(--flag-red) 66%)}
.flag-jp{background:radial-gradient(circle,var(--flag-red) 3px,#fff 3.5px)}
.flag-no{background:linear-gradient(var(--flag-blue),var(--flag-blue)) center/100% 2px no-repeat,linear-gradient(var(--flag-blue),var(--flag-blue)) 6px 0/2px 100% no-repeat,linear-gradient(#fff,#fff) center/100% 4px no-repeat,linear-gradient(#fff,#fff) 5px 0/4px 100% no-repeat,var(--flag-red)}
.flag-pl{background:linear-gradient(#fff 50%,var(--flag-red) 50%)}
.flag-world{border-radius:50%;border:1.3px solid var(--ink);width:14px!important;height:14px!important;top:10px!important}
.checkbox{width:15px;height:15px;border:1px solid #bbb;border-radius:3px;background:#fff}
.checkbox.on{border-color:var(--navy)}
.checkbox.on svg{left:2px;top:2px}
.sheet-title{top:44px;left:0;width:256px;text-align:center;font-family:"Noto Serif",serif;font-weight:400;font-size:12.5px;color:var(--ink)}
.sheet-close{top:45px;left:216px}
.save-btn{left:117px;top:500px;width:34px;height:34px;border-radius:50%;background:var(--navy);z-index:2}
.save-btn svg{left:10px;top:10px}
.scroll-thumb{left:70px;top:551px;width:110px;height:2px;background:#ddd;z-index:2}
.filter-btn{left:220px;width:22px;height:22px;border-radius:50%;background:#dfe4ea}
.filter-btn svg{left:5px;top:5px}
.row-delete{right:0;top:0;width:22px;height:33px;background:var(--danger)}
.row-delete svg{left:6px;top:11px}
/* detail screen */
.detail{width:268px;height:778px}
.search-line{top:56px;left:42px;width:208px;height:1px;background:#333}
.cover-art{left:21px;top:66px;width:213px;height:212px;background:linear-gradient(160deg,#1b2c4e 0%,#2d4f8a 45%,#1a1a22 80%)}
.side-strip{left:242px;top:66px;width:14px;height:212px;background:linear-gradient(#d52b2b 0 4%,#ddd 4% 30%,#f4f4f4 30% 40%,#2f4f9c 40% 66%,#eee 66% 97%,#2f4f9c 97%)}
.player{left:21px;top:288px;width:213px;height:24px;background:#fff;border-radius:12px}
.player .time{left:30px;top:8px;font-size:6px;color:#222}
.player .track{left:68px;top:11px;width:100px;height:2px;background:#ddd}
.player .track-fill{left:68px;top:11px;width:22px;height:2px;background:#222}
.player .knob{left:88px;top:9px;width:6px;height:6px;border-radius:50%;background:#222}
.episode-title{left:21px;top:331px;width:216px;font-family:"PT Serif",serif;font-weight:700;font-size:10.4px;line-height:15px;color:var(--ink)}
.meta{left:21px;height:10px;font-size:6.6px;line-height:10px;color:#222;white-space:nowrap}
.meta svg{position:static;vertical-align:-1px;margin-right:2px}
.meta b{font-weight:600}
.episode-body{left:21px;top:454px;width:216px;font-size:8.4px;line-height:14.4px;color:#333}
.show-card{left:21px;top:618px;width:213px;height:122px;background:#e9e9e9}
.show-avatar{left:94px;top:606px;width:24px;height:24px;background:#fff}
.show-avatar svg{left:6px;top:5px}
.show-name{left:21px;top:643px;width:213px;text-align:center;font-family:"PT Serif",serif;font-weight:700;font-size:8.8px;text-decoration:underline;color:var(--ink)}
.show-about{left:30px;top:661px;width:195px;text-align:center;font-size:7.4px;line-height:13px;color:#333}
.rss-btn{left:217px;top:730px;width:33px;height:33px;border-radius:50%;background:var(--navy)}
.rss-btn svg{left:9px;top:9px}
</style>
</head>
<body>

<!-- Screen 1: start -->
<section class="phone" style="left:34px;top:34px">
  <div class="notch"></div><div class="status-time">5:30</div>
  <div class="world-map" style="top:80px" role="img" aria-label="Dotted world map backdrop"></div>
  <div class="brand-mark" style="top:204px"></div>
  <h1 class="app-title" style="top:266px">VELVET LANTERN</h1>
  <p class="app-tagline" style="top:284px">Travel outside of your echo chamber and filter bubble,<br>listen to podcasts from around the world.</p>
  <div class="divider" style="top:314px"></div>
  <div class="lang-row" style="top:326px;border:none">
    <div class="flag flag-uk"></div><div class="label">English <span>(10850)</span></div>
    <svg class="ctrl" width="14" height="14" viewBox="0 0 14 14" fill="none" stroke="#2b5d86" stroke-width="1.2"><path d="M3 1v12M7 1v12M11 1v12"/><circle cx="3" cy="9" r="1.6" fill="#fff"/><circle cx="7" cy="4" r="1.6" fill="#fff"/><circle cx="11" cy="8" r="1.6" fill="#fff"/></svg>
  </div>
  <div class="play-btn" style="top:494px"><svg width="11" height="13" viewBox="0 0 11 13"><path d="M1 1l9 5.5L1 12z" fill="#fff"/></svg></div>
  <div class="home-bar"></div>
</section>

<!-- Screen 2: language picker -->
<section class="phone" style="left:322px;top:34px">
  <div class="notch"></div><div class="status-time">5:30</div>
  <h2 class="sheet-title">Languages</h2>
  <svg class="sheet-close" width="12" height="12" viewBox="0 0 12 12" stroke="#222" stroke-width="1.2"><path d="M1 1l10 10M11 1L1 11"/></svg>
  <div class="lang-row" style="top:66px"><div class="flag flag-world"></div><div class="label">All languages <span>(12345)</span></div><div class="ctrl checkbox"></div></div>
  <div class="lang-row" style="top:99.6px"><div class="flag flag-uk"></div><div class="label">English <span>(10850)</span></div><div class="ctrl checkbox on"><svg width="10" height="10" viewBox="0 0 10 10" fill="none" stroke="#0d3a5c" stroke-width="1.4"><path d="M1 5l3 3 5-6"/></svg></div></div>
  <div class="lang-row" style="top:133.2px"><div class="flag flag-de"></div><div class="label">Deutsch / German <span>(1085)</span></div><div class="ctrl checkbox"></div></div>
  <div class="lang-row" style="top:166.8px"><div class="flag flag-es"></div><div class="label">Español / Spanish <span>(914)</span></div><div class="ctrl checkbox on"><svg width="10" height="10" viewBox="0 0 10 10" fill="none" stroke="#0d3a5c" stroke-width="1.4"><path d="M1 5l3 3 5-6"/></svg></div></div>
  <div class="lang-row" style="top:200.4px"><div class="flag flag-fr"></div><div class="label">Français / French <span>(860)</span></div><div class="ctrl checkbox on"><svg width="10" height="10" viewBox="0 0 10 10" fill="none" stroke="#0d3a5c" stroke-width="1.4"><path d="M1 5l3 3 5-6"/></svg></div></div>
  <div class="lang-row" style="top:234px"><div class="flag flag-pt"></div><div class="label">Português / Portuguese <span>(344)</span></div><div class="ctrl checkbox"></div></div>
  <div class="lang-row" style="top:267.6px"><div class="flag flag-se"></div><div class="label">Svenska / Swedish <span>(313)</span></div><div class="ctrl checkbox"></div></div>
  <div class="lang-row" style="top:301.2px"><div class="flag flag-cn"></div><div class="label">中文 / Chinese <span>(271)</span></div><div class="ctrl checkbox"></div></div>
  <div class="lang-row" style="top:334.8px"><div class="flag flag-ru"></div><div class="label">Русский / Russian <span>(228)</span></div><div class="ctrl checkbox"></div></div>
  <div class="lang-row" style="top:368.4px"><div class="flag flag-dk"></div><div class="label">Dansk / Danish <span>(188)</span></div><div class="ctrl checkbox"></div></div>
  <div class="lang-row" style="top:402px"><div class="flag flag-nl"></div><div class="label">Nederlands / Dutch <span>(175)</span></div><div class="ctrl checkbox"></div></div>
  <div class="lang-row" style="top:435.6px"><div class="flag flag-it"></div><div class="label">Italiano / Italian <span>(167)</span></div><div class="ctrl checkbox"></div></div>
  <div class="lang-row" style="top:469.2px"><div class="flag flag-jp"></div><div class="label">日本語 / Japanese <span>(164)</span></div><div class="ctrl checkbox"></div></div>
  <div class="lang-row" style="top:502.8px"><div class="flag flag-no"></div><div class="label">Norsk / Norwegian <span>(132)</span></div><div class="ctrl checkbox"></div></div>
  <div class="lang-row" style="top:536.4px"><div class="flag flag-pl"></div><div class="label">Polski / Polish <span>(70)</span></div><div class="ctrl checkbox"></div></div>
  <div class="save-btn"><svg width="14" height="14" viewBox="0 0 14 14"><path d="M1 1h10l2 2v10H1z" fill="#fff"/><rect x="4" y="1" width="6" height="4" fill="#0d3a5c"/><rect x="3.5" y="8" width="7" height="4" fill="#0d3a5c"/></svg></div>
  <div class="scroll-thumb"></div>
</section>

<!-- Screen 3: selected languages, swipe to delete -->
<section class="phone" style="left:610px;top:34px">
  <div class="notch"></div><div class="status-time">5:30</div>
  <div class="world-map" style="top:78px" role="img" aria-label="Dotted world map backdrop"></div>
  <div class="brand-mark" style="top:190px"></div>
  <h1 class="app-title" style="top:252px">VELVET LANTERN</h1>
  <p class="app-tagline" style="top:270px">Travel outside of your echo chamber and filter bubble,<br>listen to podcasts from around the world.</p>
  <div class="divider" style="top:300px"></div>
  <div class="filter-btn" style="top:308px"><svg width="12" height="12" viewBox="0 0 14 14" fill="none" stroke="#2b5d86" stroke-width="1.3"><path d="M3 1v12M7 1v12M11 1v12"/><circle cx="3" cy="9" r="1.6" fill="#dfe4ea"/><circle cx="7" cy="4" r="1.6" fill="#dfe4ea"/><circle cx="11" cy="8" r="1.6" fill="#dfe4ea"/></svg></div>
  <div class="lang-row" style="top:329px;left:27px;width:229px"><div class="flag flag-uk"></div><div class="label">English <span>(10850)</span></div></div>
  <div class="lang-row" style="top:362.5px;left:27px;width:229px"><div class="flag flag-es"></div><div class="label">Español / Spanish <span>(914)</span></div></div>
  <div class="lang-row" style="top:396px;left:6px;width:234px"><div class="flag flag-fr"></div><div class="label">Français / French <span>(860)</span></div>
    <div class="row-delete"><svg width="10" height="11" viewBox="0 0 10 11" fill="none" stroke="#e06a6a" stroke-width="1"><path d="M1 2h8M3.5 2V1h3v1M2 2l.6 8h4.8L8 2M4 4v4M6 4v4"/></svg></div></div>
  <div class="play-btn" style="top:494px"><svg width="11" height="13" viewBox="0 0 11 13"><path d="M1 1l9 5.5L1 12z" fill="#fff"/></svg></div>
  <div class="home-bar"></div>
</section>

<!-- Screen 4: selected languages, edit list -->
<section class="phone" style="left:610px;top:610px">
  <div class="notch"></div><div class="status-time">5:30</div>
  <div class="world-map" style="top:78px" role="img" aria-label="Dotted world map backdrop"></div>
  <div class="brand-mark" style="top:190px"></div>
  <h1 class="app-title" style="top:252px">VELVET LANTERN</h1>
  <p class="app-tagline" style="top:270px">Travel outside of your echo chamber and filter bubble,<br>listen to podcasts from around the world.</p>
  <div class="divider" style="top:300px"></div>
  <div class="filter-btn" style="top:308px"><svg width="12" height="12" viewBox="0 0 14 14" fill="none" stroke="#2b5d86" stroke-width="1.3"><path d="M3 1v12M7 1v12M11 1v12"/><circle cx="3" cy="9" r="1.6" fill="#dfe4ea"/><circle cx="7" cy="4" r="1.6" fill="#dfe4ea"/><circle cx="11" cy="8" r="1.6" fill="#dfe4ea"/></svg></div>
  <div class="lang-row" style="top:329px"><div class="flag flag-uk"></div><div class="label">English <span>(10850)</span></div>
    <svg class="ctrl" width="10" height="11" viewBox="0 0 10 11" fill="none" stroke="#c4c4c4" stroke-width="1" style="top:11px"><path d="M1 2h8M3.5 2V1h3v1M2 2l.6 8h4.8L8 2M4 4v4M6 4v4"/></svg></div>
  <div class="lang-row" style="top:362.5px"><div class="flag flag-es"></div><div class="label">Español / Spanish <span>(914)</span></div>
    <svg class="ctrl" width="10" height="11" viewBox="0 0 10 11" fill="none" stroke="#c4c4c4" stroke-width="1" style="top:11px"><path d="M1 2h8M3.5 2V1h3v1M2 2l.6 8h4.8L8 2M4 4v4M6 4v4"/></svg></div>
  <div class="lang-row" style="top:396px"><div class="flag flag-fr"></div><div class="label">Français / French <span>(860)</span></div>
    <svg class="ctrl" width="10" height="11" viewBox="0 0 10 11" fill="none" stroke="#c4c4c4" stroke-width="1" style="top:11px"><path d="M1 2h8M3.5 2V1h3v1M2 2l.6 8h4.8L8 2M4 4v4M6 4v4"/></svg></div>
  <div class="play-btn" style="top:494px"><svg width="11" height="13" viewBox="0 0 11 13"><path d="M1 1l9 5.5L1 12z" fill="#fff"/></svg></div>
  <div class="home-bar"></div>
</section>

<!-- Screen 5: episode detail -->
<section class="phone detail" style="left:898px;top:34px">
  <div class="notch"></div><div class="status-time">5:30</div>
  <svg style="left:12px;top:46px" width="14" height="14" viewBox="0 0 14 14" fill="none" stroke="#222" stroke-width="1.2"><path d="M1 7l6-5.5L13 7M3 5.5V13h8V5.5"/><path d="M5.8 13V9.5h2.4V13"/></svg>
  <div class="search-line"></div>
  <svg style="left:237px;top:46px" width="12" height="12" viewBox="0 0 12 12" fill="none" stroke="#222" stroke-width="1.2"><circle cx="5" cy="5" r="4"/><path d="M8 8l3.5 3.5"/></svg>
  <svg style="left:4px;top:172px" width="12" height="10" viewBox="0 0 12 10" fill="none" stroke="#0d3a5c" stroke-width="1.3"><path d="M11 5H1M5 1L1 5l4 4"/></svg>
  <div class="cover-art" role="img" aria-label="Cover art for the Harbor Desk Nightly show from Beacon News"></div>
  <div class="side-strip" role="img" aria-label="Next podcast cover peeking in"></div>
  <div class="player">
    <svg style="left:10px;top:6px" width="12" height="12" viewBox="0 0 12 12"><rect width="12" height="12" fill="#111"/><rect x="3.5" y="3" width="1.6" height="6" fill="#fff"/><rect x="6.9" y="3" width="1.6" height="6" fill="#fff"/></svg>
    <div class="time">1:00/18.37</div>
    <div class="track"></div><div class="track-fill"></div><div class="knob"></div>
    <svg style="left:178px;top:7px" width="10" height="10" viewBox="0 0 10 10"><path d="M1 3.5h2L6 1v8L3 6.5H1z" fill="#222"/><path d="M7.5 3a2.5 2.5 0 010 4" stroke="#222" fill="none"/></svg>
    <svg style="left:195px;top:7px" width="9" height="10" viewBox="0 0 9 10"><path d="M4.5 0v6M1.8 3.5l2.7 2.7 2.7-2.7M0.5 9h8" stroke="#222" stroke-width="1.4" fill="none"/></svg>
  </div>
  <h2 class="episode-title">Lorem ipsum dolor sit amet adipiscing elit monec quis lacus tristique mauris finibus egest fringilla gravida enean lobortis</h2>
  <div class="meta" style="top:392px"><svg width="8" height="8" viewBox="0 0 8 8"><rect x="0.5" y="1" width="7" height="6.5" fill="none" stroke="#111"/><rect x="0.5" y="1" width="7" height="2" fill="#111"/><rect x="2" y="4.5" width="1" height="1" fill="#111"/><rect x="4" y="4.5" width="1" height="1" fill="#111"/></svg><b>2 days ago</b></div>
  <div class="meta" style="top:406px"><svg width="8" height="8" viewBox="0 0 8 8"><path d="M4 0.5C6.2 0.5 7.8 1.8 7.8 3.5S6.2 6.5 4 6.5L1 7.8l.8-2C.8 5.2.2 4.4.2 3.5.2 1.8 1.8.5 4 .5z" fill="#111"/></svg><b>English</b> (feed, detected)</div>
  <div class="meta" style="top:421px"><svg width="7" height="8" viewBox="0 0 7 8"><path d="M3.5 8S.3 4.8.3 3.2a3.2 3.2 0 016.4 0C6.7 4.8 3.5 8 3.5 8z" fill="#111"/><circle cx="3.5" cy="3.2" r="1.2" fill="#fff"/></svg><b>United States</b> (feed) &nbsp;| &nbsp;<b>Country</b> (ip-country) &nbsp;|</div>
  <div class="meta" style="top:432px;left:32px"><b>Country</b> (domain-country)</div>
  <p class="episode-body">Lorem ipsum dolor sit amet, consectetur adipiscing elit. Donec quis lacus non ipsum viverra tristique. Mauris finibus egestas fringilla gravida. Aenean lobs est sit amet est viverra, quis fermentum neque matt. Nunc urna urna, porttitor id conquat vitae, sodales vitae sapien. Curabitur efficitur pulvin venenatis. Nulla commodo turpis ut nibh egestas bibendum magna suscipit malesuada sagittis lectus. Fusce ut ornare enim estibulum rutrum. egestas posuere tellus enim pretium purus imperdiet ligula semper.</p>
  <div class="show-card"></div>
  <div class="show-avatar"><svg width="12" height="13" viewBox="0 0 12 13"><circle cx="6" cy="3.5" r="3" fill="#111"/><path d="M0 13c0-4 2.5-5.5 6-5.5S12 9 12 13z" fill="#111"/></svg></div>
  <h3 class="show-name">Harbor Desk Nightly</h3>
  <p class="show-about">Nullam sollicitudin porttitor enim, in imperdiet lorem feugiat at. Nulla nunc erat, gravida nec ligula dapibus tempus libero. Cras eget felis posuere, ultrices lorem a, varius dolor. Nullam interdum lacus quis augue rutrum gravida ipsum hendrerit.</p>
  <div class="rss-btn"><svg width="15" height="15" viewBox="0 0 15 15" fill="none" stroke="#fff" stroke-width="2"><circle cx="2.5" cy="12.5" r="1.5" fill="#fff" stroke="none"/><path d="M1 7a7 7 0 017 7M1 2a12 12 0 0112 12"/></svg></div>
  <div class="home-bar"></div>
</section>

</body>
</html>
```